Business Card Re-design

We are looking for a fresh bold look for general office business cards. We are a staffing agency that staffs industrial, coal mining, and clerical jobs.
Tag Line: We match the BEST people with the BEST roles.
Harlow Falls Office: 2473 W. Tallow Creek Rd, Harlow Falls, OH - 47308
p. 555.203.6180 f. 555.203.6195
Milbrook Office: 264 S. Birch Ln, Milbrook, OH - 47152
p. 555.319.2047 f. 555.203.6195
Absentee/Emergency 24hr Hotline 555.203.6172 opt.1
www.bluelanternworkforce.example

```html
<!DOCTYPE html>
<html lang="en">
<head>
<meta charset="utf-8">
<title>Blue Lantern Workforce – Business Card</title>
<link href="https://fonts.googleapis.com/css2?family=Oswald:wght@500&family=Roboto:wght@400&family=Roboto+Condensed:wght@700&display=swap" rel="stylesheet">
<style>
  :root {
    --backdrop: #d6d6d6;
    --navy: #1f2d5c;
    --navy-deep: #263566;
    --sky: #4f8db4;
    --green: #2e8b3e;
    --paper: #f4f4f3;
    --white: #ffffff;
    --ink: #2a3352;
  }
  * { margin: 0; padding: 0; box-sizing: border-box; }
  html, body { width: 1200px; height: 576px; overflow: hidden; }
  body { background: var(--backdrop); position: relative; font-family: "Roboto", sans-serif; }

  .card {
    position: absolute; top: 138px; width: 484px; height: 294px;
    border-radius: 12px; overflow: hidden;
  }
  .card--front {
    left: 82px;
    background: linear-gradient(32deg, var(--sky) 0%, #3d6496 38%, var(--navy-deep) 100%);
    color: var(--white);
  }
  .card--back { left: 602px; background: var(--paper); color: var(--ink); }

  .brand { position: absolute; display: flex; align-items: center; gap: 10px; }
  .brand__mark { width: 16px; height: 16px; flex: none; }
  .brand__name {
    font-family: "Oswald", sans-serif; font-weight: 500; text-transform: uppercase;
    line-height: 1.02; letter-spacing: 0.5px;
  }
  .card--front .brand { left: 120px; top: 76px; }
  .card--front .brand__mark { background: var(--white); }
  .card--front .brand__name { font-size: 33px; color: var(--white); }

  .card--back .brand { left: 34px; top: 104px; }
  .card--back .brand__mark { background: var(--green); }
  .card--back .brand__name { font-size: 27px; color: var(--navy); }

  .tagline { position: absolute; white-space: nowrap; }
  .card--front .tagline {
    left: 0; right: 0; top: 183px; text-align: center; font-size: 12px; color: #e6ebf4;
  }
  .card--back .tagline {
    left: 32px; top: 184px; font-family: "Roboto Condensed", sans-serif; font-weight: 700;
    font-size: 10.5px; color: var(--navy);
  }
  .website {
    position: absolute; left: 0; right: 0; top: 256px; text-align: center;
    font-size: 12px; color: #e6ebf4;
  }

  .offices { position: absolute; left: 286px; top: 44px; }
  .office + .office { margin-top: 14px; }
  .office__title {
    font-family: "Oswald", sans-serif; font-weight: 500; font-size: 17px;
    color: var(--navy); margin-bottom: 4px; letter-spacing: 0.2px;
  }
  .contact { list-style: none; }
  .contact li {
    display: flex; align-items: flex-start; gap: 10px;
    font-size: 11.5px; line-height: 16.8px; color: var(--ink); white-space: nowrap;
  }
  .contact svg { width: 12px; height: 12px; margin-top: 2px; flex: none; fill: var(--green); }
</style>
</head>
<body>
<svg width="0" height="0" style="position:absolute" aria-hidden="true">
  <defs>
    <symbol id="icon-phone" viewBox="0 0 24 24"><path d="M3 9c0-3 4-5 9-5s9 2 9 5v2h-5V8.5c-1-.4-2.4-.6-4-.6s-3 .2-4 .6V11H3z"/><path d="M6 12h12l2 8H4z"/></symbol>
    <symbol id="icon-fax" viewBox="0 0 24 24"><path d="M7 2h10v6H7z"/><path d="M3 9h18v9h-3v-3H6v3H3z"/><path d="M7 16h10v6H7z"/></symbol>
    <symbol id="icon-pin" viewBox="0 0 24 24"><path d="M12 1a8 8 0 0 0-8 8c0 6 8 14 8 14s8-8 8-14a8 8 0 0 0-8-8zm0 11a3 3 0 1 1 0-6 3 3 0 0 1 0 6z"/></symbol>
  </defs>
</svg>

<section class="card card--front" aria-label="Card front">
  <div class="brand">
    <span class="brand__mark"></span>
    <div class="brand__name">Blue Lantern<br>Workforce</div>
  </div>
  <p class="tagline">We match the BEST people with the BEST roles</p>
  <p class="website">www.bluelanternworkforce.example</p>
</section>

<section class="card card--back" aria-label="Card back">
  <div class="brand">
    <span class="brand__mark"></span>
    <div class="brand__name">Blue Lantern<br>Workforce</div>
  </div>
  <p class="tagline">We match the BEST people with the BEST roles</p>

  <div class="offices">
    <div class="office">
      <h2 class="office__title">Corporate Office</h2>
      <ul class="contact">
        <li><svg><use href="#icon-phone"/></svg>555.203.6180</li>
        <li><svg><use href="#icon-fax"/></svg>555.203.6195</li>
        <li><svg><use href="#icon-pin"/></svg><span>2473 W. Tallow Creek Rd,<br>Harlow Falls, OH - 47308</span></li>
      </ul>
    </div>
    <div class="office">
      <h2 class="office__title">Milbrook Office</h2>
      <ul class="contact">
        <li><svg><use href="#icon-phone"/></svg>555.319.2047</li>
        <li><svg><use href="#icon-fax"/></svg>555.203.6195</li>
        <li><svg><use href="#icon-pin"/></svg><span>264 S. Birch Ln,<br>Milbrook, OH - 47152</span></li>
      </ul>
    </div>
  </div>
</section>
</body>
</html>
```